Fantasy Sports Website Needs Web Design

We are modeling our site functionality from www.brisklinepicks.com using the same backend systems, and our site will be Rostervault.com with the logo branding attached.
The site should have the following pages: home page, signup pages, games/lobby, rules, live scoring, support/FAQs, contact us.
There should be navication in the footer of the page that includes the different pages along with the Privacy Policy and Terms of Use.

Target Market(s)
•	80% Male
•	89.8% Caucasian
•	51.5% Not Married
•	Average Age: 34
•	College Degree or More: 78.1%
•	51.6% play video games
•	19% play online poker
•	Stats fairly in line with young male demographic
Number of Pages Required
2 page
Look and feel
Each slider illustrates characteristics of the customer's brand and the style your logo design should communicate.

```html
<!DOCTYPE html>
<html lang="en">
<head>
<meta charset="utf-8">
<title>Roster Vault</title>
<link rel="stylesheet" href="https://fonts.googleapis.com/css2?family=Arimo:wght@400;700&family=PT+Sans:wght@400;700&display=swap">
<style>
  :root {
    --page-bg: #262626;
    --page-bg-dark: #121212;
    --panel: #000000;
    --accent: #f05a1e;
    --heading: #ffffff;
    --body-text: #8c8c8c;
    --rule: #3a3a3a;
    --icon: #5a5a5a;
    --legal: #d0d0d0;
  }
  * { margin: 0; padding: 0; box-sizing: border-box; }
  html, body { width: 1200px; height: 1048px; overflow: hidden; }
  body {
    background: radial-gradient(ellipse at 50% 40%, var(--page-bg) 0%, var(--page-bg-dark) 100%);
    font-family: "Arimo", Arial, sans-serif;
    position: relative;
  }
  .site {
    position: absolute; left: 199px; top: 0; width: 800px; height: 1048px;
    background: var(--panel);
  }
  .abs { position: absolute; }

  /* header */
  .brand {
    left: 14px; top: 46px; display: flex; align-items: center; gap: 10px;
    font-family: "PT Sans", sans-serif; font-weight: 700; font-size: 24px;
    color: var(--heading); text-transform: uppercase; letter-spacing: 1px;
  }
  .brand-mark { width: 22px; height: 22px; background: var(--accent); }
  .social { display: flex; gap: 3px; }
  .social span { width: 16px; height: 16px; background: var(--icon); border-radius: 2px; display: block; }
  .header-social { right: 21px; top: 38px; }
  .main-nav { right: 20px; top: 75px; display: flex; gap: 20px; }
  .main-nav a, .footer-nav a {
    font-family: "PT Sans", sans-serif; font-size: 13.5px; color: var(--accent); text-decoration: none;
  }

  /* hero */
  .hero {
    left: 0; top: 113px; width: 800px; height: 334px;
    background: linear-gradient(180deg, #b9b8ab 0%, #a9a595 45%, #8b7b63 75%, #b49d7a 100%);
  }
  .hero-title { left: 37px; top: 58px; font-size: 19px; font-weight: 700; color: var(--heading); }
  .hero-copy {
    left: 37px; top: 83px; width: 270px; font-size: 7px; line-height: 9.5px;
    font-weight: 700; color: var(--heading);
  }

  /* sections */
  .section-title {
    font-family: "PT Sans", sans-serif; font-size: 12.5px; color: var(--accent); text-transform: uppercase;
  }
  .section-title strong { color: var(--heading); font-weight: 400; font-size: 15px; }
  .copy { font-size: 9.5px; line-height: 13.5px; color: var(--body-text); }
  .more { color: var(--accent); display: block; font-size: 9.5px; text-decoration: none; }
  .rule {
    left: 20px; width: 770px; height: 4px;
    border-top: 1px dotted var(--rule); border-bottom: 1px dotted var(--rule);
  }
  .photo { display: block; }

  /* footer */
  .footer-nav { left: 20px; top: 963px; display: flex; gap: 21px; }
  .footer-social { right: 15px; top: 960px; }
  .legal { left: 22px; top: 988px; font-size: 10px; line-height: 12px; color: var(--legal); }
  .legal a { color: var(--legal); text-decoration: none; }
</style>
</head>
<body>
<div class="site">
  <header>
    <div class="abs brand"><span class="brand-mark"></span>Roster Vault</div>
    <div class="abs social header-social"><span></span><span></span><span></span><span></span><span></span><span></span></div>
    <nav class="abs main-nav">
      <a href="#">Home</a><a href="#">Sign Up</a><a href="#">Lobby</a><a href="#">Rules</a>
      <a href="#">Live Scoring</a><a href="#">Support/FAQs</a><a href="#">Contact</a>
    </nav>
  </header>

  <section class="abs hero" role="img" aria-label="BMX rider mid-air over a skate park under a cloudy sky">
    <h1 class="abs hero-title">ROSTER VAULT</h1>
    <p class="abs hero-copy">Draft your roster, enter daily contests and chase real cash prizes. Pick your players against the salary cap, join a game in the lobby and follow every point as it happens with live scoring all season long.</p>
  </section>

  <section class="welcome">
    <h2 class="abs section-title" style="left:20px;top:460px;">Welcome to <strong>Roster Vault</strong></h2>
    <p class="abs copy" style="left:20px;top:484px;width:568px;">Roster Vault is daily fantasy sports made simple. Sign up in minutes, browse open games in the lobby and build a lineup of your favourite players under the salary cap. Contests run every day across football, basketball, baseball and hockey, with entry fees to suit every player. Watch your lineup climb the standings with live scoring and collect your winnings when the final whistle blows. Read the rules before you play.
      <a class="more" href="#">Read More //</a></p>
    <div class="abs photo" style="left:597px;top:477px;width:189px;height:75px;background:linear-gradient(135deg,#2d6fd6,#1a3f9a);" role="img" aria-label="Rider in helmet waving against a blue sky"></div>
  </section>

  <div class="abs rule" style="top:570px;"></div>

  <section class="lobby">
    <h2 class="abs section-title" style="left:20px;top:600px;">Whats included - Games lobby</h2>
    <div class="abs photo" style="left:20px;top:627px;width:220px;height:146px;background:linear-gradient(180deg,#e6e9ec,#6b7a6a);" role="img" aria-label="BMX rider jumping above a crowd"></div>
    <div class="abs photo" style="left:250px;top:627px;width:223px;height:145px;background:linear-gradient(180deg,#4d6b3e,#a9b2c8);" role="img" aria-label="Skateboarder riding a bowl"></div>
    <div class="abs photo" style="left:481px;top:627px;width:227px;height:142px;background:radial-gradient(circle at 85% 20%,#3b6fb8,#0b1024 70%);" role="img" aria-label="Aerial silk performer"></div>
  </section>

  <div class="abs rule" style="top:810px;"></div>

  <section class="about">
    <h2 class="abs section-title" style="left:20px;top:833px;">About <strong>Roster Vault</strong></h2>
    <p class="abs copy" style="left:20px;top:860px;width:520px;">Roster Vault has one simple goal in mind: fair, fast fantasy sports for every fan. We run daily and weekly contests on a proven platform, so games open on time and payouts land quickly. Head-to-head matchups, leagues and big tournaments all sit in one lobby. Our support team and FAQs are ready to help with anything from signup to scoring, so you can spend less time waiting and more time building the winning lineup.</p>
  </section>

  <section class="news">
    <h2 class="abs section-title" style="left:548px;top:834px;">News &amp; Events</h2>
    <p class="abs copy" style="left:548px;top:860px;width:245px;">New weekend tournaments open Friday with bigger prize pools and guaranteed payouts for every sport
      <a class="more" href="#">Read More //</a></p>
  </section>

  <div class="abs rule" style="top:948px;height:1px;border-bottom:none;"></div>

  <footer>
    <nav class="abs footer-nav">
      <a href="#">Home</a><a href="#">Sign Up</a><a href="#">Lobby</a><a href="#">Rules</a>
      <a href="#">Live Scoring</a><a href="#">Support/FAQs</a><a href="#">Contact</a>
    </nav>
    <div class="abs social footer-social"><span></span><span></span><span></span><span></span><span></span><span></span></div>
    <p class="abs legal">COPYRIGHT 2013. ALL RIGHTS RESERVED.<br><a href="#">TERMS OF USE</a> &nbsp;-&nbsp; <a href="#">PRIVACY POLICY</a> &nbsp;-&nbsp; <a href="#">DISCLAIMER</a></p>
  </footer>
</div>
</body>
</html>
```